Bref créative
Larkfield Joint & Motion Medicine
Letterhead, stationary and card design
Professional
Dr. Paul Korvitz
Director
418 West 71st Street
New York, NY 10187
director@larkfieldjoint.com
larkfieldjoint.com
Here is the logo file for use with the project

```html
<!DOCTYPE html>
<html lang="en">
<head>
<meta charset="utf-8">
<title>Larkfield Joint &amp; Motion Medicine – Stationery</title>
<link href="https://fonts.googleapis.com/css2?family=Questrial&display=swap" rel="stylesheet">
<style>
  :root {
    --backdrop: #e4e5e7;
    --paper: #ffffff;
    --navy-deep: #141a3c;
    --navy: #232c5c;
    --blue-glow: #4f86c6;
    --gold-dark: #5a3a12;
    --gold: #b07a2a;
    --gold-light: #d9a550;
    --ink: #23295a;
    --mark-fill: #2a2f4e;
    --faint: #f1f2f4;
  }
  * { margin: 0; padding: 0; box-sizing: border-box; }
  html, body { width: 1200px; height: 840px; overflow: hidden; }
  body {
    background: var(--backdrop);
    font-family: "Questrial", "Century Gothic", sans-serif;
    position: relative;
  }
  .sheet {
    position: absolute;
    background: var(--paper);
    box-shadow: 0 6px 18px rgba(0,0,0,0.18);
    overflow: hidden;
  }
  .sheet > svg.decor { position: absolute; inset: 0; width: 100%; height: 100%; }

  .brand { position: absolute; display: flex; align-items: center; gap: 8px; }
  .brand-dot {
    border-radius: 50%;
    background: radial-gradient(circle at 40% 35%, #4a4f70, var(--mark-fill));
    flex: none;
  }
  .brand-name {
    color: var(--ink);
    text-transform: uppercase;
    letter-spacing: 0.04em;
    line-height: 1.1;
  }

  .contact {
    position: absolute;
    color: #fff;
    font-style: normal;
    line-height: 1.55;
    white-space: nowrap;
  }

  /* Letterhead */
  .letterhead { left: 50px; top: 96px; width: 500px; height: 647px; }
  .letterhead .brand { left: 22px; top: 22px; }
  .letterhead .brand-dot { width: 30px; height: 30px; }
  .letterhead .brand-name { font-size: 12px; width: 130px; }
  .letterhead .watermark {
    position: absolute; left: 140px; top: 250px;
    width: 220px; height: 220px; border-radius: 50%;
    background: var(--faint);
  }
  .letterhead .contact { left: 20px; bottom: 16px; font-size: 6.5px; }

  /* Envelope */
  .envelope { left: 590px; top: 96px; width: 560px; height: 243px; }
  .envelope .brand { left: 22px; top: 62px; }
  .envelope .brand-dot { width: 28px; height: 28px; }
  .envelope .brand-name { font-size: 12px; width: 130px; }
  .envelope .flap-dot {
    position: absolute; left: 268px; top: 12px;
    width: 24px; height: 24px; border-radius: 50%;
    background: radial-gradient(circle at 40% 35%, #6d7396, #3a4066);
  }
  .envelope .contact { left: 20px; bottom: 14px; font-size: 6.5px; }

  /* Business cards */
  .card { top: 540px; width: 240px; height: 137px; }
  .card-front { left: 640px; }
  .card-back { left: 900px; background: linear-gradient(180deg, var(--navy) 0%, var(--navy-deep) 55%, #0d1130 100%); }
  .card-front .brand { left: 14px; top: 12px; gap: 6px; }
  .card-front .brand-dot { width: 20px; height: 20px; }
  .card-front .brand-name { font-size: 8px; width: 100px; }
  .card-front .person { position: absolute; left: 18px; top: 50px; color: var(--ink); font-size: 6px; line-height: 1.4; }
  .card-front .contact { left: 18px; bottom: 10px; font-size: 5.5px; }
  .card-back .site {
    position: absolute; left: 0; right: 0; top: 40px;
    text-align: center; color: #d5d9ea; font-size: 6px; letter-spacing: 0.05em;
  }
  .card-back .back-dot {
    position: absolute; left: 107px; top: 56px;
    width: 26px; height: 26px; border-radius: 50%;
    background: radial-gradient(circle at 40% 35%, #6d7396, #2f3560);
  }
</style>
</head>
<body>

<section class="sheet letterhead" aria-label="Letterhead">
  <svg class="decor" viewBox="0 0 500 647" preserveAspectRatio="none">
    <defs>
      <linearGradient id="lh-navy" x1="0" y1="0" x2="1" y2="0">
        <stop offset="0" stop-color="#1b2350"/>
        <stop offset="0.55" stop-color="#2f4a86"/>
        <stop offset="0.75" stop-color="#4f86c6"/>
        <stop offset="1" stop-color="#141a3c"/>
      </linearGradient>
      <linearGradient id="lh-gold" x1="0" y1="0" x2="1" y2="1">
        <stop offset="0" stop-color="#d9a550"/>
        <stop offset="0.5" stop-color="#b07a2a"/>
        <stop offset="1" stop-color="#5a3a12"/>
      </linearGradient>
    </defs>
    <path d="M200 0 C260 0 265 30 330 34 L500 38 L500 0 Z" fill="url(#lh-navy)"/>
    <path d="M0 585 L120 585 C175 585 180 612 195 630 C205 642 215 647 230 647 L0 647 Z" fill="url(#lh-gold)"/>
  </svg>
  <div class="watermark"></div>
  <div class="brand">
    <span class="brand-dot"></span>
    <span class="brand-name">Larkfield Joint &amp; Motion Medicine</span>
  </div>
  <address class="contact">
    418 West 71st Street, New York, NY 10187<br>
    Tel 212.555.0148 &nbsp; Fax 212.555.0149<br>
    director@larkfieldjoint.com<br>
    larkfieldjoint.com
  </address>
</section>

<section class="sheet envelope" aria-label="Envelope">
  <svg class="decor" viewBox="0 0 560 243" preserveAspectRatio="none">
    <defs>
      <linearGradient id="env-navy" x1="0" y1="0" x2="1" y2="0">
        <stop offset="0" stop-color="#141a3c"/>
        <stop offset="0.45" stop-color="#2a3c78"/>
        <stop offset="0.62" stop-color="#4f86c6"/>
        <stop offset="1" stop-color="#141a3c"/>
      </linearGradient>
      <linearGradient id="env-gold" x1="0" y1="0" x2="1" y2="1">
        <stop offset="0" stop-color="#d9a550"/>
        <stop offset="0.5" stop-color="#b07a2a"/>
        <stop offset="1" stop-color="#5a3a12"/>
      </linearGradient>
    </defs>
    <path d="M0 0 L560 0 L560 95 C520 80 480 60 420 56 L0 50 Z" fill="url(#env-navy)"/>
    <path d="M0 172 L175 172 C205 172 212 198 222 220 C229 236 238 243 252 243 L0 243 Z" fill="url(#env-gold)"/>
  </svg>
  <span class="flap-dot"></span>
  <div class="brand">
    <span class="brand-dot"></span>
    <span class="brand-name">Larkfield Joint &amp; Motion Medicine</span>
  </div>
  <address class="contact">
    418 West 71st Street, New York, NY 10187<br>
    Tel 212.555.0148 &nbsp; Fax 212.555.0149<br>
    director@larkfieldjoint.com<br>
    larkfieldjoint.com
  </address>
</section>

<section class="sheet card card-front" aria-label="Business card front">
  <svg class="decor" viewBox="0 0 240 137" preserveAspectRatio="none">
    <defs>
      <linearGradient id="card-gold" x1="0" y1="0" x2="1" y2="1">
        <stop offset="0" stop-color="#d9a550"/>
        <stop offset="0.5" stop-color="#b07a2a"/>
        <stop offset="1" stop-color="#5a3a12"/>
      </linearGradient>
      <linearGradient id="card-navy" x1="0" y1="0" x2="1" y2="0">
        <stop offset="0" stop-color="#2a3c78"/>
        <stop offset="0.6" stop-color="#4f86c6"/>
        <stop offset="1" stop-color="#141a3c"/>
      </linearGradient>
    </defs>
    <path d="M150 0 C175 0 180 10 205 12 L240 14 L240 0 Z" fill="url(#card-navy)"/>
    <path d="M0 90 L170 90 C200 90 205 110 215 125 C220 133 228 137 240 137 L0 137 Z" fill="url(#card-gold)"/>
  </svg>
  <div class="brand">
    <span class="brand-dot"></span>
    <span class="brand-name">Larkfield Joint &amp; Motion Medicine</span>
  </div>
  <p class="person">Dr. Paul Korvitz<br>Director</p>
  <address class="contact">
    418 West 71st Street, New York, NY 10187<br>
    Tel 212.555.0148 &nbsp; Fax 212.555.0149<br>
    director@larkfieldjoint.com
  </address>
</section>

<section class="sheet card card-back" aria-label="Business card back">
  <p class="site">larkfieldjoint.com</p>
  <span class="back-dot"></span>
</section>

</body>
</html>
```